Fresh pet feed direct from manufacturer to door step. Quality and Freshness un-surpassed in Industr

Need Business Card Design; leading into many other projects, for New Franchised Business Opportunity providing home delivery of fresh dog and cat feed (no emphasis needed for cat) direct from manufacturing facility. (no middle men or distributors) Food is Farm to Factory fresh. Our trademarked tagline is "Ranch Fresh to Your Door ! "
Updates

Please take note of other contest for Chirplane Cover and Profile Pic's

Target Market(s)

Dog and Cat owners

Industry/Entity Type

Pet

Contact Information for Business Card

Name, address, local phone, national 800 number, website, email address

Other font styles liked:
• follow that from logo

Requirements
Must have
• Our feed is made in Texas with ingredients sourced from local farms. We want to lean heavy on the Made in West Texas , ranch theme but that has a 'black label', 'vantrel', 'premium', 'high-end' look and feel
Nice to have
• maybe have an offer on card? 20% off with promo code "x" etc.. ?? just a thought...

```html
<!DOCTYPE html>
<html lang="en">
<head>
<meta charset="utf-8">
<title>Harlow's Reserve — Business Card</title>
<link href="https://fonts.googleapis.com/css2?family=Marcellus+SC&family=Crimson+Text:wght@400;600&display=swap" rel="stylesheet">
<style>
  :root {
    --backdrop: #2c2e31;
    --plum: #231a2b;
    --plum-deep: #1a1320;
    --gold: #a88540;
    --paper: #ffffff;
    --ink: #1d1a20;
    --shadow: rgba(0, 0, 0, 0.45);
  }
  html, body {
    margin: 0;
    width: 1200px;
    height: 900px;
    overflow: hidden;
    background: var(--backdrop);
  }
  .stage {
    position: relative;
    width: 1200px;
    height: 900px;
  }
  .card {
    position: absolute;
    left: 230px;
    top: 235px;
    width: 740px;
    height: 430px;
    background: var(--paper);
    box-shadow: 0 18px 40px var(--shadow);
    overflow: hidden;
  }
  .card__band {
    position: absolute;
    left: 0;
    top: 0;
    width: 100%;
    height: 150px;
    background: linear-gradient(180deg, var(--plum) 0%, var(--plum-deep) 100%);
    border-bottom: 4px solid var(--gold);
  }
  .brand {
    position: absolute;
    left: 56px;
    top: 52px;
    display: flex;
    align-items: center;
    gap: 14px;
  }
  .brand__dot {
    width: 18px;
    height: 18px;
    border-radius: 50%;
    background: var(--paper);
  }
  .brand__name {
    font-family: "Marcellus SC", serif;
    font-size: 40px;
    line-height: 1;
    color: var(--paper);
    letter-spacing: 1px;
  }
  .person {
    position: absolute;
    right: 70px;
    top: 48px;
  }
  .person__name {
    font-family: "Marcellus SC", serif;
    font-weight: 400;
    font-size: 26px;
    color: var(--paper);
    letter-spacing: 1px;
    margin: 0;
  }
  .person__role {
    font-family: "Crimson Text", serif;
    font-size: 17px;
    color: var(--gold);
    margin: 2px 0 0 20px;
  }
  .tagline {
    position: absolute;
    left: 70px;
    top: 302px;
    font-family: "Marcellus SC", serif;
    font-size: 20px;
    color: var(--ink);
    letter-spacing: 0.5px;
    margin: 0;
  }
  .contact {
    position: absolute;
    left: 468px;
    top: 196px;
    font-family: "Crimson Text", serif;
    font-size: 18px;
    color: var(--ink);
    line-height: 1.2;
  }
  .contact__address {
    margin: 0 0 22px;
    font-style: normal;
  }
  .contact__list {
    list-style: none;
    margin: 0;
    padding: 0;
  }
  .contact__item {
    display: flex;
    align-items: center;
    gap: 8px;
    height: 22px;
  }
  .contact__icon {
    width: 14px;
    height: 14px;
    fill: var(--gold);
    flex: none;
  }
</style>
</head>
<body>
<main class="stage">
  <article class="card">
    <div class="card__band"></div>

    <div class="brand">
      <span class="brand__dot"></span>
      <span class="brand__name">Harlow's Reserve</span>
    </div>

    <div class="person">
      <h1 class="person__name">Wade Callister</h1>
      <p class="person__role">Managing Director</p>
    </div>

    <p class="tagline">“Ranch Fresh to Your Door”</p>

    <div class="contact">
      <address class="contact__address">4180 Mesquite Ridge Road<br>Lubbock TX 79407</address>
      <ul class="contact__list">
        <li class="contact__item">
          <svg class="contact__icon" viewBox="0 0 16 16" aria-hidden="true"><path d="M3.5 1.5l2.4 2.8-1.2 1.8c.8 1.8 2.4 3.4 4.2 4.2l1.8-1.2 2.8 2.4-1.4 2.4C7 13.4 2.6 9 1.1 3z"/></svg>
          <span>+ 800 555 0142</span>
        </li>
        <li class="contact__item">
          <svg class="contact__icon" viewBox="0 0 16 16" aria-hidden="true"><path d="M1 5c2-3 12-3 14 0l-1 2h-3V5.5H5V7H2z"/><rect x="3" y="8" width="10" height="6" rx="1"/></svg>
          <span>+ 806 555 0199</span>
        </li>
        <li class="contact__item">
          <svg class="contact__icon" viewBox="0 0 16 16" aria-hidden="true"><path d="M1 3h14v10H1z M2.5 4.5L8 9l5.5-4.5" stroke="#fff" stroke-width="1.2"/></svg>
          <span>info@harlowsreserve.com</span>
        </li>
        <li class="contact__item">
          <svg class="contact__icon" viewBox="0 0 16 16" aria-hidden="true"><circle cx="8" cy="8" r="7"/><path d="M1 8h14M8 1c-3 4-3 10 0 14M8 1c3 4 3 10 0 14" stroke="#fff" stroke-width="1" fill="none"/></svg>
          <span>www.harlowsreserve.com</span>
        </li>
      </ul>
    </div>
  </article>
</main>
</body>
</html>
```